cover for CD- Single.

This design is for a CD cover. The design is at your disposal, using all of your creative talents.
Things to improve the photo: Cleaning the face, removing blemishes.
Design in black and white would be an option (Color would be another option). I reiterate it is up to your taste and criteria, any reform and art on the cover of Cd.
Name of the single: El Camino del Silencio
Artist Name: Marisol Duarte

Target Market(s)

Single Music

Industry/Entity Type

Music

Colors

Designer to choose colors to be used in the design.

Requirements
Must have
• style, elegance, professionalism, spontaneity
Nice to have
• I want it to be as professional as possible.
Should not have
• Spelling errors.

```html
<!DOCTYPE html>
<html lang="es">
<head>
<meta charset="utf-8">
<title>El Camino del Silencio — Marisol Duarte</title>
<link rel="stylesheet" href="https://fonts.googleapis.com/css2?family=Playfair+Display:wght@500&family=Raleway:wght@300;400&family=Mrs+Saint+Delafield&display=swap">
<style>
  :root {
    --page-bg: #f3f3f3;
    --cover-black: #050505;
    --photo-mid: #6e6e6e;
    --photo-light: #b9b9b9;
    --title-white: #ffffff;
    --gold-light: #f3d56b;
    --gold-mid: #d4a92a;
    --gold-dark: #9c7414;
    --caption-grey: #cfcfcf;
  }
  * { margin: 0; padding: 0; box-sizing: border-box; }
  html, body {
    width: 693px;
    height: 1200px;
    overflow: hidden;
    background: var(--page-bg);
  }
  .canvas {
    position: relative;
    width: 693px;
    height: 1200px;
  }
  .cover {
    position: absolute;
    left: 115px;
    top: 368px;
    width: 463px;
    height: 463px;
    overflow: hidden;
    background: var(--cover-black);
    box-shadow: 0 2px 8px rgba(0,0,0,0.18);
  }
  .cover-photo {
    position: absolute;
    inset: 0;
    background:
      radial-gradient(ellipse 55% 45% at 62% 30%, var(--photo-light) 0%, var(--photo-mid) 45%, transparent 80%),
      linear-gradient(180deg, #2a2a2a 0%, #151515 55%, var(--cover-black) 100%);
  }
  .cover-shade {
    position: absolute;
    inset: 0;
    background: linear-gradient(180deg, rgba(0,0,0,0) 45%, rgba(0,0,0,0.75) 78%, rgba(0,0,0,0.95) 100%);
  }
  .side-strip {
    position: absolute;
    left: 22px;
    top: 20px;
    display: flex;
    flex-direction: row;
    align-items: flex-end;
    gap: 6px;
    writing-mode: vertical-rl;
    transform: rotate(180deg);
    transform-origin: center;
  }
  .side-note {
    font-family: "Raleway", sans-serif;
    font-weight: 400;
    font-size: 6.5px;
    line-height: 1.3;
    color: var(--title-white);
  }
  .release-year {
    font-family: "Raleway", sans-serif;
    font-weight: 300;
    font-size: 30px;
    letter-spacing: 1px;
    color: var(--gold-mid);
  }
  .title-block {
    position: absolute;
    left: 0;
    right: 0;
    top: 266px;
    text-align: center;
  }
  .single-title {
    font-family: "Playfair Display", serif;
    font-weight: 500;
    color: var(--title-white);
    line-height: 0.9;
  }
  .single-title .line-one {
    display: block;
    font-size: 38px;
    letter-spacing: 0.5px;
  }
  .single-title .line-two {
    display: block;
    font-size: 56px;
  }
  .artist-name {
    margin-top: -22px;
    font-family: "Mrs Saint Delafield", cursive;
    font-weight: 400;
    font-size: 54px;
    line-height: 1;
    background: linear-gradient(100deg, var(--gold-dark) 0%, var(--gold-light) 35%, var(--gold-mid) 60%, var(--gold-light) 80%, var(--gold-dark) 100%);
    -webkit-background-clip: text;
    background-clip: text;
    color: transparent;
  }
  .liner-note {
    position: absolute;
    left: 0;
    right: 0;
    top: 424px;
    text-align: center;
    font-family: "Raleway", sans-serif;
    font-size: 6px;
    line-height: 1.45;
    color: var(--caption-grey);
  }
</style>
</head>
<body>
<main class="canvas">
  <section class="cover">
    <div class="cover-photo" role="img" aria-label="Black and white portrait photograph of the singer with eyes closed, hand raised near her face, soft bokeh lights around"></div>
    <div class="cover-shade"></div>

    <div class="side-strip">
      <p class="side-note">Nuevo sencillo disponible<br>en todas las plataformas</p>
      <p class="release-year">2021</p>
    </div>

    <header class="title-block">
      <h1 class="single-title">
        <span class="line-one">El Camino del</span>
        <span class="line-two">Silencio</span>
      </h1>
      <p class="artist-name">Marisol Duarte</p>
    </header>

    <p class="liner-note">Producido y grabado en estudio durante el invierno. Letra y música originales,<br>arreglos de cuerdas y piano, mezcla y masterización final del sencillo.</p>
  </section>
</main>
</body>
</html>
```